Full Service Day Spa Needs Wordpress Template Designed

Verdant Spa is a full service day spa, where we make our own line of bath and body products. The current website houses an online store with an TradeNook base (as a WordPress plugin) and simple web pages with information and price lists for services.
For the upgraded website, we are doing a significant makeover and want to include the ability to have full screen video on our main page, windowed or full screen video on feature pages (for example, pages for "Meet our staff" or "Product Demos")
The site should retain standard WordPress compatibility for plugins, such as galleries etc.
The ability to include iframes would be considered a plus so that we can embed external scheduling applications that we subscribe to.
The color scheme for our spa features chocolate brown, taupe, cream, and turquoise for color accents. We would like our website to reflect these colors as our customers find them relaxing.
Our spa has a number of paintings on our walls, which could be used for inspiration for the website design. We like modern abstract art, with curves and swirls. I have included examples of this artwork so that potential designers can see what we like.
The new site must include our logo (provided) and our tag line: "Come Relax With Us" displayed in the upper left in the header.
We would prefer to have the option to put the menu either on the left side, or across the top to the right of the logo.
Words to describe the look we are seeking would be elegant, upscale, relaxing.

Target Market(s)

Our market is primarily local women (in and around our city) who are professionals aged 30 - 65.

Industry/Entity Type

Store

Colors
f78f20
00a990
f37022

Requirements
Must have
• The template should accommodate full screen and partial screen HTML5 video. Must have a menu, could be top or could be side. Should be in shades of browns and neutral colors, with teal accents, or similar highlights to the attached pictures of our artwork we have in the spa. We are looking for a consistent look that our customers can identify is us. Must have our logo in the upper left side of the header.
Nice to have
• Iframes built in would be nice, although we know we can get plugins for that. Likewise we know we can get plugins for the HTML 5 video, we would like the template built with accommodating that in mind. We have seen sites that have full screen video on the main page. We think this looks good.
Should not have
• We are looking for something elegant and upscale, so we are not looking for something "Cartoonish".

```html
<!DOCTYPE html>
<html lang="en">
<head>
<meta charset="utf-8">
<title>Verdant Spa</title>
<link href="https://fonts.googleapis.com/css2?family=Noto+Sans:wght@400;700&family=Noto+Serif:ital,wght@0,400;0,700;1,400;1,700&display=swap" rel="stylesheet">
<style>
:root{
  --cream:#eeeae0;
  --cream-light:#f6f3ec;
  --taupe:#7d6e63;
  --chocolate:#3a2620;
  --chocolate-mid:#4b342c;
  --turquoise:#2ad0d6;
  --teal-star:#1aa7a8;
  --text:#3b2c26;
  --muted:#6a5a52;
  --white:#ffffff;
}
*{margin:0;padding:0;box-sizing:border-box}
html,body{width:890px;height:1200px;overflow:hidden}
body{position:relative;background:var(--cream);font-family:"Noto Sans",sans-serif;color:var(--text)}
.abs{position:absolute}
.backdrop{left:0;top:0;width:890px;height:433px;background:linear-gradient(100deg,#e6ddcf 0%,#efe9df 35%,#e9e1d5 70%,#d9c8b8 100%)}
.header-band{left:0;top:0;width:890px;height:98px;background:rgba(246,243,236,.78);border-bottom:1px solid rgba(180,165,150,.4)}
.tagline{left:90px;top:26px;font-family:"Noto Serif",serif;font-weight:700;font-style:italic;font-size:20px;color:var(--chocolate)}
.tagline .q{font-size:18px;vertical-align:6px;margin:0 3px}
.search{left:389px;top:33px;width:268px;height:22px;border:1px solid #cfc7bb;background:rgba(255,255,255,.7);font-family:"Noto Serif",serif;font-style:italic;font-size:9px;color:#8a7d74;padding:5px 10px}
.search svg{position:absolute;right:7px;top:4px}
.logo{left:705px;top:14px;width:100px;text-align:center}
.logo .mark{width:40px;height:40px;border-radius:50%;background:var(--taupe);margin:0 auto 6px}
.logo .name{font-family:"Noto Serif",serif;font-size:17px;color:var(--chocolate)}
.nav{left:79px;top:74px;display:flex;font-size:9px;color:var(--chocolate);height:22px;align-items:center}
.nav span{padding:0 9.5px;line-height:22px}
.nav .active{background:var(--chocolate);color:var(--white);font-weight:700}
.hero-main{left:79px;top:143px;width:362px;height:251px;background:linear-gradient(180deg,#3c3a3b,#2c2a2a 60%,#4d4038)}
.play{left:15px;top:15px;width:42px;height:25px;background:#fbf6d3;display:flex;align-items:center;justify-content:center}
.hero-title{left:15px;top:182px;font-family:"Noto Serif",serif;font-style:italic;font-weight:700;font-size:15px;color:var(--turquoise)}
.hero-text{left:15px;top:208px;width:320px;font-family:"Noto Serif",serif;font-size:9.2px;line-height:14px;color:var(--white)}
.hero-a{left:454px;top:143px;width:190px;height:119px;background:linear-gradient(160deg,#cfd4d3,#8aa0a2 60%,#b9b3aa)}
.hero-b{left:454px;top:275px;width:190px;height:119px;background:linear-gradient(160deg,#c6a890,#d9a3ab 60%,#6f5e4f)}
.hero-c{left:657px;top:143px;width:153px;height:251px;background:linear-gradient(170deg,#b6a58c,#d8cfc3 45%,#c44a45 75%,#a8a091)}
.welcome{left:0;top:433px;width:890px;height:101px;background:var(--taupe);text-align:center;color:var(--white);font-family:"Noto Serif",serif}
.welcome h1{font-size:15px;font-weight:700;margin-top:17px;color:#f7efd8}
.welcome p{font-size:9.5px;line-height:15.5px;margin-top:11px;color:#f1e9de}
.cat{top:561px;width:199px;height:107px;overflow:hidden}
.cat .label{position:absolute;left:0;bottom:0;width:100%;height:24px;background:rgba(60,45,38,.72);font-family:"Noto Serif",serif;font-style:italic;font-size:13px;color:var(--white);padding:3px 10px}
.cat .go{position:absolute;right:0;bottom:0;width:28px;height:24px;background:rgba(60,45,38,.6);display:flex;align-items:center;justify-content:center}
.cat .go.on{background:var(--turquoise)}
.card{width:147px;height:185px;background:var(--white);text-align:center}
.card .img{height:92px}
.card h3{font-weight:400;font-size:11.5px;margin-top:10px;color:var(--text)}
.card .stars{font-size:11px;letter-spacing:5px;color:var(--teal-star);margin-top:6px;padding-left:5px}
.card .stars b{color:var(--chocolate);font-weight:400}
.card .desc{font-size:9.5px;margin-top:4px}
.card .price{font-size:10px;margin-top:5px;color:var(--muted)}
.footer-links{left:0;top:1114px;width:890px;height:39px;background:var(--white)}
.crumbs{left:124px;top:14px;font-size:8.3px;color:var(--muted)}
.crumbs i{font-style:normal;color:#b5aaa1;margin:0 4px}
.crumbs .first{color:var(--chocolate)}
.social{left:690px;top:12px;display:flex;gap:9px}
.social span{width:12px;height:12px;background:#1e2a44;display:block}
.footer-bar{left:0;top:1153px;width:890px;height:47px;background:var(--chocolate-mid)}
.email{left:124px;top:12px;width:152px;height:23px;background:var(--cream);font-family:"Noto Serif",serif;font-style:italic;font-size:8px;color:#6f625a;padding:7px 8px}
.signup{left:276px;top:12px;width:66px;height:23px;background:var(--turquoise);font-size:10px;color:var(--chocolate);display:flex;align-items:center;justify-content:center;gap:5px}
.copy{right:124px;top:18px;font-size:8px;color:#d6c9bf}
</style>
</head>
<body>
<div class="abs backdrop" role="img" aria-label="Soft beach with stacked stones"></div>

<header class="abs header-band"></header>
<div class="abs tagline"><span class="q">&ldquo;</span>Come Relax With Us<span class="q">&rdquo;</span></div>
<div class="abs search">Search...
  <svg width="12" height="12" viewBox="0 0 12 12"><circle cx="7" cy="5" r="3.6" fill="none" stroke="#3a2620" stroke-width="1.4"/><line x1="4.4" y1="7.6" x2="1" y2="11" stroke="#3a2620" stroke-width="1.6"/></svg>
</div>
<div class="abs logo"><div class="mark"></div><div class="name">Verdant</div></div>
<nav class="abs nav">
  <span class="active">Home</span><span>Price List</span><span>Store Hours &amp; Contact</span><span>Bath and Body Products</span><span>On Sale!</span><span>The Goods On Our Services</span><span>Jobs Listing</span>
</nav>

<section class="abs hero-main" role="img" aria-label="Storefront of Verdant Spa">
  <div class="abs play"><svg width="10" height="11" viewBox="0 0 10 11"><path d="M0 0L10 5.5L0 11Z" fill="#2a1d18"/></svg></div>
  <div class="abs hero-title">Lorem ipsum dolor sit amet</div>
  <p class="abs hero-text">Quisque quis egestas nulla. Sed at laoreet felis. Cum sociis natoque penatibus et magnilos dis parturient montes, nascetur ridiculus mus.</p>
</section>
<div class="abs hero-a" role="img" aria-label="Display table of bottled products"></div>
<div class="abs hero-b" role="img" aria-label="Rows of lotion bottles"></div>
<div class="abs hero-c" role="img" aria-label="Holiday gift mug wrapped with a red bow"></div>

<section class="abs welcome">
  <h1>Welcome to Verdant Spa</h1>
  <p>Verdant Spa is a full service day spa with registered massage therapists, comprehensive esthetical services,<br>and our own exclusive line of custom hand made bath and body products.</p>
</section>

<div class="abs cat" style="left:124px;background:linear-gradient(180deg,#4fb3e6,#bfe4f5 55%,#d9c6b8)" role="img" aria-label="Hot stone massage">
  <div class="label">Spa</div>
  <div class="go on"><svg width="16" height="12" viewBox="0 0 16 12"><path d="M0 0L16 6L0 12L3 6Z" fill="#2a1d18"/></svg></div>
</div>
<div class="abs cat" style="left:346px;background:linear-gradient(160deg,#e8cdbf,#d8b4a2 60%,#c9a18f)" role="img" aria-label="Facial treatment">
  <div class="label">Beauty</div>
  <div class="go"><svg width="16" height="12" viewBox="0 0 16 12"><path d="M0 0L16 6L0 12L3 6Z" fill="#2a1d18"/></svg></div>
</div>
<div class="abs cat" style="left:567px;background:linear-gradient(160deg,#ded8d0,#c5bdb3 60%,#a59c92)" role="img" aria-label="Treatment chair in a clinic room">
  <div class="label">Personal Care</div>
  <div class="go"><svg width="16" height="12" viewBox="0 0 16 12"><path d="M0 0L16 6L0 12L3 6Z" fill="#2a1d18"/></svg></div>
</div>

<div class="abs card" style="left:124px;top:698px"><div class="img" style="background:linear-gradient(160deg,#2b2624,#3d3532)" role="img" aria-label="Braided bracelet"></div><h3>Songbird Bracelet</h3><div class="stars">★★★★<b>★</b></div><div class="desc">Bracelets, necklaces</div><div class="price">From $8.95</div></div>
<div class="abs card" style="left:289px;top:698px"><div class="img" style="background:linear-gradient(160deg,#c9b08f,#dc9ea4 55%,#6d5b4d)" role="img" aria-label="Massage cream bottles"></div><h3>Massage Cream</h3><div class="stars">★★★★<b>★</b></div><div class="desc">Professional Series</div><div class="price">From $59.99</div></div>
<div class="abs card" style="left:454px;top:698px"><div class="img" style="background:linear-gradient(160deg,#4a4560,#e9e3d4 55%,#6e6a80)" role="img" aria-label="Tin of muscle balm"></div><h3>Muscle Balm</h3><div class="stars">★★★★<b>★</b></div><div class="desc">Excellent for sore muscles</div><div class="price">From $10.99</div></div>
<div class="abs card" style="left:618px;top:698px"><div class="img" style="background:linear-gradient(160deg,#efe3e6,#d89aa6 45%,#8fc36a)" role="img" aria-label="Wrapped bath truffles"></div><h3>Medium Bath Truffles</h3><div class="stars">★★★★<b>★</b></div><div class="desc">These are a LOT larger</div><div class="price">From $4.99</div></div>

<div class="abs card" style="left:124px;top:901px"><div class="img" style="background:linear-gradient(160deg,#d23d9c,#5c3fb0 55%,#2b2a6e)" role="img" aria-label="Sequined gift bag"></div><h3>Hand to Toes Gift Set</h3><div class="stars">★★★★<b>★</b></div><div class="desc">Special this holiday season</div><div class="price">From $14.99</div></div>
<div class="abs card" style="left:289px;top:901px"><div class="img" style="background:linear-gradient(160deg,#ece8e0,#d9d3c6 50%,#5a5fa8)" role="img" aria-label="Jar of body scrub"></div><h3>Sea Mineral Body Scrub</h3><div class="stars">★★★★<b>★</b></div><div class="desc">Salt scrub is big moisturizing</div><div class="price">From $20.99</div></div>
<div class="abs card" style="left:454px;top:901px"><div class="img" style="background:linear-gradient(160deg,#f3f1ec,#c9b9a8 50%,#8a5a6a)" role="img" aria-label="Jar of hand treatment"></div><h3>Quick Hand Renewal</h3><div class="stars">★★★★<b>★</b></div><div class="desc">Treat yourself spa experience</div><div class="price">From $10.99</div></div>
<div class="abs card" style="left:618px;top:901px"><div class="img" style="background:linear-gradient(160deg,#9fd0df,#3d5fa8 40%,#e8a0c0 70%,#f2e6b0)" role="img" aria-label="Bars of handmade soap"></div><h3>Cold Process Soap</h3><div class="stars">★★★★<b>★</b></div><div class="desc">Pumpkin Bread CP soap</div><div class="price">From $4.99</div></div>

<footer>
  <div class="abs footer-links">
    <div class="abs crumbs"><span class="first">Home</span><i>/</i>Price List<i>/</i>Store Hours &amp; Contact<i>/</i>Bath and Body Products<i>/</i>On Sale!<i>/</i>The Goods On Our Services<i>/</i>Jobs Listing</div>
    <div class="abs social"><span></span><span></span><span></span><span></span></div>
  </div>
  <div class="abs footer-bar">
    <div class="abs email">Enter email address</div>
    <div class="abs signup">Sign up <svg width="14" height="12" viewBox="0 0 14 12"><path d="M0 5L14 0L10 12L7 7Z" fill="#2a1d18"/></svg></div>
    <div class="abs copy">© 2014 Verdant Spa., All Rights Reserved</div>
  </div>
</footer>
</body>
</html>
```